QORLIN Business card. A.I. company developing trading strategies.

My name is marcello bianchi and I'm CEO and co-founder of QORLIN Research, an AI company focusing on generating Ai-driven trading strategies.
This is our website: https://qorlin-analytics.example/
Values of our company: tech & R&D driven (we're all very mathy/stats/data driven), sophisticated (we only look for sophisticated, high knowledge investors), reserved (we don't go around telling anyone what we do).
Our main product: PivotFund. A trading strategy that delivered 70% in 2022 and 20% in 2023 so far.
Our main potential clients: HNW individuals, hedge funds, asset managers, tech entrepreneur.
Target Market(s)
Hedge funds, asset managers, High Net Worth individuals, Pension funds
Contact Information for Business Card
The basic: name, job title, company name, address, mail, phone number

```html
<!DOCTYPE html>
<html lang="en">
<head>
<meta charset="utf-8">
<title>QORLIN Research – Business Card</title>
<link href="https://fonts.googleapis.com/css2?family=Poppins:wght@300;400;500;600&display=swap" rel="stylesheet">
<style>
  :root {
    --canvas: #e4e4e4;
    --paper: #f7f7f7;
    --ink: #111111;
    --accent: #c8102e;
    --night: #0a0a0a;
    --night-soft: #222222;
    --rule: #9a9a9a;
  }
  * { margin: 0; padding: 0; box-sizing: border-box; }
  html, body { width: 1200px; height: 930px; overflow: hidden; }
  body {
    background: var(--canvas);
    font-family: "Poppins", Arial, sans-serif;
    display: flex;
    align-items: center;
    justify-content: center;
    gap: 48px;
  }
  .card {
    width: 525px;
    height: 300px;
    position: relative;
    box-shadow: 0 2px 10px rgba(0,0,0,0.12);
  }
  /* Front side */
  .card--front {
    background: var(--paper);
    color: var(--ink);
    display: flex;
    flex-direction: column;
    align-items: center;
    padding-top: 40px;
  }
  .wordmark {
    font-weight: 300;
    font-size: 40px;
    letter-spacing: 6px;
    line-height: 1;
    color: var(--ink);
  }
  .wordmark--light { color: #f2f2f2; }
  .holder-name {
    margin-top: 28px;
    font-weight: 600;
    font-size: 17px;
    letter-spacing: 1px;
  }
  .holder-role {
    font-size: 13px;
    color: var(--accent);
    margin-top: 2px;
  }
  .details {
    margin-top: 22px;
    display: flex;
    align-items: stretch;
    gap: 14px;
    font-size: 11.5px;
    line-height: 1.5;
  }
  .contact-list {
    list-style: none;
    text-align: right;
  }
  .contact-list li {
    display: flex;
    justify-content: flex-end;
    align-items: center;
    gap: 6px;
  }
  .contact-icon { width: 11px; height: 11px; fill: var(--accent); }
  .divider { width: 1px; background: var(--rule); }
  .address { font-style: normal; }
  .address-company { color: var(--accent); }

  /* Back side */
  .card--back {
    background: radial-gradient(ellipse at 60% 60%, var(--night-soft) 0%, var(--night) 70%);
    display: flex;
    align-items: center;
    justify-content: center;
  }
  .back-texture {
    position: absolute;
    inset: 0;
    background: radial-gradient(ellipse at 62% 62%, rgba(120,120,120,0.18) 0%, rgba(0,0,0,0) 55%);
  }
  .card--back .wordmark { position: relative; }
</style>
</head>
<body>
  <section class="card card--front">
    <div class="wordmark">QORLIN</div>
    <div class="holder-name">BIANCHI</div>
    <div class="holder-role">CEO and Co-founder</div>
    <div class="details">
      <ul class="contact-list">
        <li>614 228 903
          <svg class="contact-icon" viewBox="0 0 24 24" aria-hidden="true"><path d="M6.6 10.8a15 15 0 0 0 6.6 6.6l2.2-2.2a1 1 0 0 1 1-.25 11.4 11.4 0 0 0 3.6.57 1 1 0 0 1 1 1V20a1 1 0 0 1-1 1A17 17 0 0 1 3 4a1 1 0 0 1 1-1h3.5a1 1 0 0 1 1 1c0 1.25.2 2.45.57 3.57a1 1 0 0 1-.25 1z"/></svg>
        </li>
        <li>office@qorlinresearch.example
          <svg class="contact-icon" viewBox="0 0 24 24" aria-hidden="true"><path d="M2 5h20v14H2z M2 5l10 8 10-8" fill="var(--accent)" stroke="#fff" stroke-width="1.5"/></svg>
        </li>
        <li>www.qorlin-analytics.example
          <svg class="contact-icon" viewBox="0 0 24 24" aria-hidden="true"><circle cx="12" cy="12" r="10"/><path d="M2 12h20M12 2c3 3 3 17 0 20M12 2c-3 3-3 17 0 20" fill="none" stroke="#fff" stroke-width="1.3"/></svg>
        </li>
      </ul>
      <span class="divider"></span>
      <address class="address">
        <div class="address-company">QORLIN Research</div>
        <div>12 Rue des Tilleuls</div>
        <div>75005 PARIS 5</div>
      </address>
    </div>
  </section>

  <section class="card card--back">
    <div class="back-texture" role="img" aria-label="Dark field with a faint network of connected points"></div>
    <div class="wordmark wordmark--light">QORLIN</div>
  </section>
</body>
</html>
```